New Flyer for Bin Washing Service

I would like a flyer for a new service we are launching - trash bin cleaning. It needs to be informative about what the service entails, as well as the schedules available and pricing. I have attached our logo and would like the design to be bold and modern, using the logo colors.

Below is some information about our service:
Service plans:
Monthly - $19.95
Bi-Monthly (6 times per year) - $27.95
Quarterly (4 times per year) - $35.95
One Time Cleaning - $39.00

Service is performed on the day after trash and recycling services.

More than their bad smells, filthy trash cans serve as breeding grounds for flies, mold, ants, rodents and germs. At Harbor Lawn & Yard Works, LLC, we make use of 190° hot water and an environmentally friendly cleaning process to clean, sanitize and deodorize your bins. Simply sign up and you don’t have to do anything extra! We come to your curbside and leave your trash cans sanitized, clean and smelling fresh!

This is a commercial voiceover script containing more info about our service:

All garbage cans have one common problem.
They smell! Bacteria, grime, and nasty odors build up and no one wants to deal with that! But Harbor Lawn and Yard Works has found the perfect solution for this problem! Introducing our new trash bin cleaning service!
We will properly clean and sanitize the entire surface of your trash bin. Here’s how it works!
First off, our courteous driver fits your bins into our specialized cleaning truck!
After that, the exterior of the bin is properly washed and sanitized along with the handles.
Then the interior of the bin is washed off with superheated water at a pressure of 3500 PSI.
Lastly, a deodorizing spray is applied and your bins are returned, cleaned, and sanitized, smelling fresh!

What are you waiting for? Our eco-friendly service is guaranteed to make your cans happy!

So, contact us and get your garbage cans cleaned today!

Business info:
Harbor Lawn & Yard Works, LLC
41 W. Brantley, Alton, IL 62002
618-555-0193
www.harborlawnyard.example

Target Market(s)

40+ yo homeowners, most likely women

Industry/Entity Type

Pressure Cleaning

Font styles to use
Sans Serif

Colors
0455a3
9bcb3c

Requirements
Must have
• info on pricing/schedules. Basic info on what service entails. business and contact info. Additional graphics of cans, cans before and after, or of cans being cleaned.

```html
<!DOCTYPE html>
<html lang="en">
<head>
<meta charset="utf-8">
<title>Trash Bin Cleaning Flyer</title>
<link rel="stylesheet" href="https://fonts.googleapis.com/css2?family=Oswald:wght@500;700&family=Open+Sans:ital,wght@0,400;0,600;0,700;0,800;1,700&display=swap">
<style>
  :root {
    --blue: #0455a3;
    --blue-deep: #03437f;
    --green: #9bcb3c;
    --green-deep: #5fa52a;
    --silver: #c9ccd1;
    --ink: #2b2b2b;
    --paper: #ffffff;
    --backdrop: #e4e5e7;
  }
  * { box-sizing: border-box; margin: 0; padding: 0; }
  html, body { width: 1200px; height: 1083px; overflow: hidden; }
  body { background: var(--backdrop); font-family: "Open Sans", sans-serif; }

  .flyer {
    position: absolute; left: 232px; top: 18px;
    width: 736px; height: 1046px;
    background: var(--paper); overflow: hidden;
    box-shadow: 0 6px 24px rgba(0,0,0,.18);
  }
  .flyer-shapes { position: absolute; inset: 0; }

  .brand {
    position: absolute; left: 48px; top: 40px;
    display: flex; align-items: center; gap: 12px;
  }
  .brand-dot { width: 34px; height: 34px; border-radius: 50%; background: var(--green); }
  .brand-name {
    font-family: "Oswald", sans-serif; font-weight: 700;
    font-size: 30px; line-height: 1.05; color: var(--blue); text-transform: uppercase;
  }

  .photo {
    position: absolute; border-radius: 50%;
    border: 9px solid var(--silver);
  }
  .photo-truck-street {
    left: 380px; top: 70px; width: 380px; height: 380px;
    background: radial-gradient(circle at 55% 45%, #8fb95a 0%, #5e7d46 30%, #8c8a84 60%, #d8cdb8 100%);
  }
  .photo-truck-crew {
    left: 412px; top: 468px; width: 280px; height: 280px;
    background: radial-gradient(circle at 50% 45%, #d9e43a 0%, #4f8a3c 35%, #5a6a5a 70%, #9aa0a2 100%);
  }
  .photo-before-after {
    left: 28px; top: 872px; width: 172px; height: 172px;
    border: 6px solid var(--blue);
    background: linear-gradient(180deg, #6f767c 0%, #4a5259 48%, #c9d0d4 52%, #7d868c 100%);
  }
  .mascot {
    position: absolute; left: 204px; top: 870px; width: 112px; height: 166px;
    border-radius: 18px 18px 10px 10px;
    background: linear-gradient(180deg, #a6d64a 0%, var(--green-deep) 100%);
  }

  .title { position: absolute; left: 78px; top: 196px; color: var(--paper); }
  .title-line {
    font-family: "Oswald", sans-serif; font-weight: 700;
    font-size: 66px; line-height: 1; letter-spacing: 1px;
  }
  .title-highlight {
    display: inline-block; margin-top: 6px; margin-left: -14px;
    background: var(--green); padding: 2px 14px 6px; border-radius: 6px;
    font-size: 74px;
  }

  .plans-heading {
    position: absolute; left: 60px; top: 380px;
    font-weight: 800; font-size: 30px; color: var(--paper); letter-spacing: 1px;
  }
  .plans { position: absolute; left: 44px; top: 428px; width: 300px; list-style: none; }
  .plan {
    position: relative; height: 26px; margin-bottom: 6px;
    border: 2px solid var(--paper); border-radius: 14px;
    display: flex; align-items: center; padding-left: 12px;
    font-family: "Oswald", sans-serif; font-weight: 500; font-size: 14px;
    color: var(--paper); text-transform: uppercase;
  }
  .plan small { text-transform: none; font-size: 13px; margin-left: 4px; }
  .plan-price {
    position: absolute; right: -12px; top: -4px;
    background: var(--paper); border-radius: 16px; padding: 3px 6px;
  }
  .plan-price span {
    display: block; background: var(--green); border-radius: 12px;
    color: var(--paper); font-family: "Oswald", sans-serif; font-weight: 700;
    font-size: 17px; line-height: 20px; padding: 0 10px;
  }

  .info { position: absolute; left: 40px; color: var(--ink); }
  .info-schedule {
    top: 626px; width: 362px;
    border-left: 2px solid var(--green); padding-left: 10px;
  }
  .info-process { top: 768px; width: 660px; }
  .info h2 {
    font-weight: 700; font-size: 14px; line-height: 1.3; color: var(--blue);
    margin-bottom: 5px;
  }
  .info-process h2 { font-size: 14.5px; }
  .info p { font-size: 9.4px; line-height: 1.4; }

  .cta { position: absolute; left: 398px; top: 866px; width: 330px; text-align: center; }
  .cta-question { font-weight: 800; font-size: 18px; line-height: 1.3; color: var(--blue); }
  .cta-promise {
    font-family: "Oswald", sans-serif; font-weight: 500; font-size: 11px;
    line-height: 1.4; white-space: nowrap;
    color: var(--green-deep); margin-top: 1px;
  }
  .cta-box {
    margin-top: 4px; border: 2px solid var(--blue); padding: 3px 4px;
    font-family: "Oswald", sans-serif; font-weight: 700; font-size: 11px;
    line-height: 1.3; white-space: nowrap;
    color: var(--blue); background: var(--paper);
  }
  .phone {
    position: absolute; left: 400px; top: 942px; height: 38px; width: 316px;
    background: var(--green); border-radius: 20px;
    display: flex; align-items: center; gap: 12px; padding-left: 3px;
    font-family: "Oswald", sans-serif; font-weight: 700; font-size: 30px; color: var(--paper);
  }
  .phone-icon {
    width: 32px; height: 32px; border-radius: 50%; background: var(--paper);
    display: flex; align-items: center; justify-content: center;
  }
  .business {
    position: absolute; left: 452px; top: 984px;
    color: var(--paper); font-size: 11px; line-height: 1.3; font-style: normal;
  }
  .business h3 { font-size: 12px; font-weight: 700; line-height: 1.3; }
</style>
</head>
<body>
<main class="flyer">
  <svg class="flyer-shapes" viewBox="0 0 736 1046" width="736" height="1046" aria-hidden="true">
    <path d="M0 146 Q260 204 560 104 L736 56 L736 64 Q420 222 0 156 Z" fill="var(--silver)"/>
    <path d="M0 156 Q300 216 560 112 L736 64 L736 770 Q600 720 520 650 Q320 526 0 574 Z" fill="var(--blue)"/>
    <path d="M0 570 Q320 520 520 646 L520 680 Q300 574 0 622 Z" fill="var(--green)"/>
    <path d="M0 900 Q180 864 380 896 Q330 980 300 1046 L0 1046 Z" fill="var(--green)"/>
    <path d="M0 892 Q180 856 380 888 L380 896 Q180 864 0 900 Z" fill="var(--silver)"/>
    <path d="M300 1046 Q460 960 736 868 L736 1046 Z" fill="var(--blue)"/>
  </svg>

  <header class="brand">
    <span class="brand-dot"></span>
    <span class="brand-name">Harbor Lawn<br>&amp; Yard Works</span>
  </header>

  <div class="photo photo-truck-street" role="img" aria-label="Photo of a crew loading green bins into a garbage truck on a city street"></div>
  <div class="photo photo-truck-crew" role="img" aria-label="Photo of workers in safety vests behind a green garbage truck"></div>

  <h1 class="title">
    <span class="title-line">TRASH BIN</span><br>
    <span class="title-line title-highlight">CLEANING</span>
  </h1>

  <p class="plans-heading">SERVICE PLANS:</p>
  <ul class="plans">
    <li class="plan">Monthly -<span class="plan-price"><span>$19.95</span></span></li>
    <li class="plan">Bi-Monthly<small>(6 times per year) -</small><span class="plan-price"><span>$27.95</span></span></li>
    <li class="plan">Quarterly<small>(4 times per year) -</small><span class="plan-price"><span>$35.95</span></span></li>
    <li class="plan">One Time Cleaning -<span class="plan-price"><span>$39.00</span></span></li>
  </ul>

  <section class="info info-schedule">
    <h2>Service Is Performed On<br>The Day After Trash And Recycling Services.</h2>
    <p>More than their bad smells, filthy trash cans serve as breeding grounds for flies, mold, ants, rodents and germs. At Harbor Lawn &amp; Yard Works, LLC, we make use of 190° hot water and an environmentally friendly cleaning process to clean, sanitize and deodorize your bins. Simply sign up and you don’t have to do anything extra! We come to your curbside and leave your trash cans sanitized, clean and smelling fresh!</p>
  </section>

  <section class="info info-process">
    <h2>This Is A Commercial Voiceover Script Containing More Info About Our Service:</h2>
    <p>All garbage cans have one common problem. They smell! Bacteria, grime, and nasty odors build up and no one wants to deal with that! But Harbor Lawn and Yard Works has found the perfect solution for this problem! Introducing our new trash bin cleaning service! We will properly clean and sanitize the entire surface of your trash bin. Here’s how it works! First off, our courteous driver fits your bins into our specialized cleaning truck! After that, the exterior of the bin is properly washed and sanitized along with the handles. Then the interior of the bin is washed off with superheated water at a pressure of 3500 PSI. Lastly, a deodorizing spray is applied and your bins are returned, cleaned, and sanitized, smelling fresh!</p>
  </section>

  <div class="photo photo-before-after" role="img" aria-label="Before and after photos of a trash bin interior being cleaned"></div>
  <div class="mascot" role="img" aria-label="Illustration of a smiling green trash bin character giving a thumbs up"></div>

  <section class="cta">
    <p class="cta-question">What are you waiting for?</p>
    <p class="cta-promise">Our eco-friendly service is guaranteed to make your cans happy!</p>
    <p class="cta-box">SO, CONTACT US AND GET YOUR GARBAGE CANS CLEANED TODAY!</p>
  </section>

  <div class="phone">
    <span class="phone-icon">
      <svg width="18" height="18" viewBox="0 0 24 24" aria-hidden="true"><path fill="var(--blue)" d="M6.6 10.8a15.1 15.1 0 0 0 6.6 6.6l2.2-2.2c.3-.3.7-.4 1-.2 1.1.4 2.3.6 3.6.6.6 0 1 .4 1 1V20c0 .6-.4 1-1 1A17 17 0 0 1 3 4c0-.6.4-1 1-1h3.5c.6 0 1 .4 1 1 0 1.3.2 2.5.6 3.6.1.3 0 .7-.2 1z"/></svg>
    </span>
    618-555-0193
  </div>

  <address class="business">
    <h3>Business info:</h3>
    Harbor Lawn &amp; Yard Works, LLC<br>
    41 W. Brantley, Alton, IL 62002<br>
    www.harborlawnyard.example
  </address>
</main>
</body>
</html>
```